OTT TV and VOD Service Website (like Kestrova.tv ; Vexo etc.)

Site will be used as a marketing page integrated with subscription processing (Quandle). Looking for someone with solid experience in designing video content driven sites. For the looks; clean, modern, black background with rich "popping" VOD and live TV channel titles.

Video-on-demand and international live TV channel subscribers in Asia

Coded - Design and coding required

5+ page

• See files

Requirements
Must have
• Start with an awesome looking "coming soon" page, featuring a logo on black background with video (i.e. a movie trailers) playing in the background. This page should also have an understated "about" link and an email "contact" form.
Site: Scrollable interfaces: Service / Live Channels / VOD / Subscribe.
Contrasting backgrounds as the page is being scrolled. Black as a dominating background color. See Kestrova.tv site for inspiration
There will be contact form (Register)
Nice to have
• Dynamic video background on the home page (trailer / title / channel promo)
Clear interface separation between live TV channels and VOD
Should not have
• Typical template looking scrolling site with boring icons and

```html
<!DOCTYPE html>
<html lang="en">
<head>
<meta charset="utf-8">
<title>Zarvio.TV</title>
<link href="https://fonts.googleapis.com/css2?family=Nunito+Sans:wght@300;400;600;700;800&display=swap" rel="stylesheet">
<style>
:root{
  --black:#0d0d0d;
  --white:#ffffff;
  --orange:#f7a21b;
  --orange-deep:#ee5a0e;
  --blue-light:#5bb8f7;
  --blue:#3f8ef5;
  --green-light:#72d10a;
  --green:#2e9414;
  --grey-dark:#3b3b3b;
  --footer:#2c2c2c;
  --copy:#1f1f1f;
  --muted:#cfcfcf;
}
*{box-sizing:border-box;margin:0;padding:0}
html,body{width:1200px;height:4380px;overflow:hidden;background:var(--black)}
body{font-family:"Nunito Sans",sans-serif;color:var(--white);position:relative}
.abs{position:absolute}
section,header,footer{position:absolute;left:0;width:1200px;overflow:hidden}

/* nav */
.site-nav{top:0;height:90px;background:var(--black)}
.brand{left:64px;top:18px;font-size:40px;font-weight:700;display:flex;align-items:center;gap:10px}
.brand .dot{width:14px;height:14px;border-radius:50%;background:var(--white);display:inline-block}
.menu{left:286px;top:0;height:90px;display:flex}
.menu a{color:var(--white);text-decoration:none;font-size:17px;display:flex;align-items:center;padding:0 26px;border-right:1px solid #2a2a2a;height:90px}
.menu a.active{color:var(--orange)}
.login{left:1050px;top:28px}

/* hero */
.hero{top:90px;height:614px}
.hero-photo{inset:0;background:radial-gradient(circle at 20% 25%,#4d6a86 0,#2a3340 22%,transparent 45%),radial-gradient(circle at 75% 55%,#6b3a1c 0,#2a1508 50%,#120a05 100%)}
.hero h1{left:115px;top:160px;font-size:46px;line-height:54px;font-weight:700}
.hero p{left:115px;top:282px;font-size:24px;line-height:30px;font-weight:300}
.btn-orange{background:linear-gradient(90deg,var(--orange),var(--orange-deep));color:var(--white);border-radius:30px;font-weight:700;display:flex;align-items:center;justify-content:center}
.hero .btn-orange{left:115px;top:371px;width:290px;height:52px;font-size:15px}

/* about */
.about{top:704px;height:624px;background:linear-gradient(110deg,var(--blue-light),var(--blue))}
.about h2{left:662px;top:156px;font-size:36px;font-weight:700}
.about p{left:666px;font-size:15px;line-height:27px;width:450px;color:#eaf4ff}
.btn-outline{border:2px solid var(--white);border-radius:26px;color:var(--white);font-size:15px;display:flex;align-items:center;justify-content:center}
.about .btn-outline{left:664px;top:403px;width:174px;height:48px}

/* live */
.live{top:1328px;height:588px;background:radial-gradient(circle at 65% 35%,#4a4a4a 0,#222 60%,#141414 100%)}
.live h2{left:118px;top:140px;font-size:37px;font-weight:700}
.live p{left:121px;font-size:15px;line-height:27px;width:390px}
.btn-white{background:var(--white);color:#111;border-radius:28px;font-size:14px;font-weight:600;display:flex;align-items:center;justify-content:center}
.live .btn-white{left:118px;top:388px;width:198px;height:54px}
.channels{left:560px;top:118px;width:590px;display:grid;grid-template-columns:repeat(4,1fr);row-gap:58px}
.channels span{text-align:center;font-size:29px;font-weight:800;letter-spacing:.5px;height:40px}

/* shows */
.shows{top:1916px;height:422px;background:linear-gradient(90deg,#2e2e2e,#0e0e0e)}
.section-title{width:1200px;text-align:center;font-size:33px;font-weight:700}
.shows .section-title{top:48px}
.show{top:122px;width:396px;height:298px}
.play{width:76px;height:76px;border-radius:50%;background:var(--white);left:160px;top:111px}
.play svg{position:absolute;left:28px;top:22px}
.arrow{top:250px}

/* movies */
.movies{top:2338px;height:513px;background:linear-gradient(180deg,#1a1a1a,#3a3a3a)}
.movies .section-title{top:56px}
.genres{left:74px;top:126px;display:grid;grid-template-columns:repeat(4,252px);grid-auto-rows:153px;gap:10px}
.genre{display:flex;align-items:center;justify-content:center;font-size:23px;font-weight:700}

/* pricing */
.pricing{top:2851px;height:629px;background:linear-gradient(120deg,var(--green-light),var(--green))}
.pricing .section-title{top:68px;color:#ffb01f;font-size:37px}
.tag{width:116px;height:42px;border-radius:22px;background:linear-gradient(90deg,var(--orange),var(--orange-deep));color:var(--white);font-size:20px;font-weight:700;display:flex;align-items:center;justify-content:center}
.price{font-size:31px;font-weight:700;color:#333}
.price s{font-size:19px;color:var(--orange-deep);margin-left:4px}
.feat{font-size:14px;line-height:18px;color:#444}
.tick{color:var(--orange);font-weight:800}
.btn-trial{width:118px;height:40px;border:2px solid var(--orange-deep);border-radius:22px;color:var(--orange-deep);font-size:15px;font-weight:700;display:flex;align-items:center;justify-content:center}

/* contact */
.contact{top:3480px;height:515px;background:var(--grey-dark)}
.contact .section-title{top:90px}
.field{border:2px solid #5fc71a;border-radius:14px;font-size:15px;color:#ddd;padding:15px 26px}
.contact .btn-orange{left:513px;top:356px;width:168px;height:50px;font-size:21px}

/* footer */
.site-footer{top:3995px;height:309px;background:var(--footer)}
.site-footer .brand{left:133px;top:68px;font-size:40px}
.socials{left:138px;top:152px;display:flex;gap:6px}
.socials span{width:33px;height:33px;border:2px solid var(--white);border-radius:50%}
.col{top:72px;font-size:14px;line-height:23px;color:var(--muted)}
.col h4{font-size:15px;font-weight:700;color:var(--white);margin-bottom:8px}
.copyright{top:4304px;height:76px;background:var(--copy);display:flex;align-items:center;justify-content:center;font-size:13px;color:#aaa}
</style>
</head>
<body>

<header class="site-nav">
  <div class="abs brand">Zarvio.TV <span class="dot"></span></div>
  <nav class="abs menu">
    <a class="active">About</a><a>Live TV</a><a>TV Shows</a><a>Movies</a><a>Watch</a><a>Special Offer</a>
  </nav>
  <svg class="abs login" width="26" height="28" viewBox="0 0 26 28" fill="none" stroke="#fff" stroke-width="2"><path d="M10 2h13v24H10"/><path d="M2 14h13M11 9l5 5-5 5"/></svg>
</header>

<section class="hero">
  <div class="abs hero-photo" role="img" aria-label="Family watching a film together on a projector screen in a dim living room"></div>
  <h1 class="abs">Great Selection of best<br>TV shows and movies</h1>
  <p class="abs">Watch thousands of shows and movies<br>with you family at anywhere</p>
  <a class="abs btn-orange">GET YOUR FREE TRIAL NOW</a>
</section>

<section class="about">
  <svg class="abs" style="left:130px;top:30px" width="500" height="520" viewBox="0 0 500 520" role="img" aria-label="Mosaic of video thumbnails shaped as a play button">
    <defs><linearGradient id="mosaic" x1="0" y1="0" x2="1" y2="1"><stop offset="0" stop-color="#3a4a66"/><stop offset=".5" stop-color="#8a5a4a"/><stop offset="1" stop-color="#1e2a3e"/></linearGradient></defs>
    <path d="M10 40 Q10 0 50 15 L470 235 Q495 260 470 285 L50 505 Q10 520 10 480 Z" fill="url(#mosaic)"/>
  </svg>
  <h2 class="abs">What is Zarvio.TV</h2>
  <p class="abs" style="top:220px">Augiat in pede Fusce tellus Sed metus augue convallis et vehicula ut pulvinar eu ante Integer orci tellus tristique vitae</p>
  <p class="abs" style="top:288px">mauris viverra in gravida eu mattis in ante Morbi eget arcurmentum vel congue id euismod in elit Fusce ultricies orci ac feugiat suscipit leo massa sodales velit et</p>
  <a class="abs btn-outline">LEARN MORE</a>
</section>

<section class="live">
  <div class="abs" style="inset:0;background:rgba(0,0,0,.35)" role="img" aria-label="Group of friends cheering while watching television"></div>
  <svg class="abs" style="left:0;top:0" width="540" height="588" viewBox="0 0 540 588">
    <defs><linearGradient id="orangeFill" x1="0" y1="0" x2="1" y2="0"><stop offset="0" stop-color="#f4a00c"/><stop offset="1" stop-color="#ee5a0e"/></linearGradient></defs>
    <path d="M0 0 H260 C460 40 560 250 520 380 C490 480 420 550 360 588 H0 Z" fill="url(#orangeFill)"/>
  </svg>
  <h2 class="abs">Live Channels</h2>
  <p class="abs" style="top:210px">Augiat in pede Fusce tellus Sed metus augue convallis et vehicula ut pulvinar eu ante Integer orc</p>
  <p class="abs" style="top:278px">mauris viverra in gravida eu mattis in ante Morbi eget arcurmentum vel congue id euismod in elit Fusce ultricies orci ac feugiat suscipit</p>
  <a class="abs btn-white">CHANNEL LINEUP</a>
  <div class="abs channels">
    <span>Arvo</span><span>Lumo</span><span>Cresta</span><span>Vistaro</span>
    <span>Newsa</span><span>Dreamly</span><span>Sportiva</span><span>Dishly</span>
    <span>Halo</span><span>Nestly</span><span>Epoch</span><span>Indie</span>
    <span>Nova</span><span>Gridline</span><span>Marquee</span><span>Stellar</span>
  </div>
</section>

<section class="shows">
  <h2 class="abs section-title">Popular TV Shows</h2>
  <div class="abs show" style="left:0;background:linear-gradient(135deg,#5a3a2e,#2a1a22)" role="img" aria-label="Friends gathered in a lively bar scene">
    <div class="abs play"><svg width="26" height="32"><path d="M0 0L26 16L0 32Z" fill="#111"/></svg></div>
  </div>
  <div class="abs show" style="left:402px;background:radial-gradient(circle at 50% 55%,#3a6ae0,#101a4a 70%)" role="img" aria-label="Brightly lit television studio stage">
    <div class="abs play" style="top:95px"><svg width="26" height="32"><path d="M0 0L26 16L0 32Z" fill="#111"/></svg></div>
  </div>
  <div class="abs show" style="left:804px;background:linear-gradient(135deg,#2a3a8a,#141a40)" role="img" aria-label="Two presenters on a talent show stage">
    <div class="abs play" style="left:150px;top:110px"><svg width="26" height="32"><path d="M0 0L26 16L0 32Z" fill="#111"/></svg></div>
  </div>
  <svg class="abs arrow" style="left:14px" width="20" height="34"><path d="M17 2L3 17L17 32" stroke="#fff" stroke-width="4" fill="none"/></svg>
  <svg class="abs arrow" style="left:1156px" width="20" height="34"><path d="M3 2L17 17L3 32" stroke="#fff" stroke-width="4" fill="none"/></svg>
</section>

<section class="movies">
  <h2 class="abs section-title">Best Movies</h2>
  <div class="abs genres">
    <div class="genre" style="background:linear-gradient(135deg,#8a3a2a,#c98a5a)" role="img" aria-label="Surfer riding a wave at sunset">Latest</div>
    <div class="genre" style="background:linear-gradient(135deg,#3a5a7a,#9ab0c0)" role="img" aria-label="Snowboarder mid-jump">Action</div>
    <div class="genre" style="background:linear-gradient(135deg,#1a1a1a,#3a3530)" role="img" aria-label="Actors on a dark stage">Drama</div>
    <div class="genre" style="background:linear-gradient(135deg,#c9a56a,#8a6a3a)" role="img" aria-label="Child with a kite in a golden field">Kids</div>
    <div class="genre" style="background:linear-gradient(135deg,#6a1a2a,#1a2030)" role="img" aria-label="Theatre masks under red light">Comedy</div>
    <div class="genre" style="background:linear-gradient(135deg,#1e2430,#2e3648)" role="img" aria-label="Dark misty forest">Horror</div>
    <div class="genre" style="background:linear-gradient(135deg,#c9502a,#6a2a1a)" role="img" aria-label="Red alien landscape">Sci-Fi</div>
    <div class="genre" style="background:linear-gradient(135deg,#7a8a9a,#9a2a2a)" role="img" aria-label="Vintage car on an old street">Classic</div>
  </div>
</section>

<section class="pricing">
  <h2 class="abs section-title">Our Pricing</h2>
  <svg class="abs" style="left:200px;top:140px" width="800" height="430" viewBox="0 0 800 430">
    <path d="M360 10 Q392 0 392 45 V385 Q392 430 350 420 L25 250 Q0 215 25 185 L330 20 Z" fill="#fff"/>
    <path d="M440 10 Q408 0 408 45 V385 Q408 430 450 420 L775 250 Q800 215 775 185 L470 20 Z" fill="#fff"/>
  </svg>
  <div class="abs tag" style="left:430px;top:240px">Basic</div>
  <div class="abs price" style="left:382px;top:298px">$14.95<s>$19.95</s></div>
  <div class="abs feat" style="left:360px;top:356px">Features 80 live channels <span class="tick">✓</span></div>
  <div class="abs feat" style="left:323px;top:390px">14 days archive for all channels <span class="tick">✓</span></div>
  <div class="abs btn-trial" style="left:431px;top:442px">Free Trial</div>

  <div class="abs tag" style="left:646px;top:240px">Best</div>
  <div class="abs price" style="left:647px;top:298px">$19.95<s>$24.95</s></div>
  <div class="abs feat" style="left:648px;top:350px;font-size:13px"><span class="tick">✓</span> Everything in Basic + over 150 live channels</div>
  <div class="abs feat" style="left:648px;top:384px;font-size:13px;width:290px"><span class="tick">✓</span> Hundreds of popular TV shows<br>&nbsp;&nbsp;&nbsp;and feature films</div>
  <div class="abs btn-trial" style="left:646px;top:440px">Free Trial</div>
</section>

<section class="contact">
  <h2 class="abs section-title">Ask a Question</h2>
  <div class="abs field" style="left:174px;top:158px;width:412px;height:50px">Your Name</div>
  <div class="abs field" style="left:174px;top:221px;width:412px;height:50px">Email address</div>
  <div class="abs field" style="left:174px;top:284px;width:412px;height:50px">Phone Number</div>
  <div class="abs field" style="left:606px;top:158px;width:414px;height:176px">Message</div>
  <a class="abs btn-orange">Submit</a>
</section>

<footer class="site-footer">
  <div class="abs brand">Zarvio.TV <span class="dot"></span></div>
  <div class="abs socials"><span></span><span></span><span></span><span></span></div>
  <div class="abs col" style="left:386px"><h4>GET TV</h4>Features<br>Live TV<br>TV Shows<br>Movies<br>Watch<br>Special Offer</div>
  <div class="abs col" style="left:550px"><h4>SERVICES</h4>Pellentesque<br>Faucibus Ut<br>Accumsan ultri<br>Enim vestibulum<br>Non fermentum</div>
  <div class="abs col" style="left:719px"><h4>RESOURCES</h4>Support<br>Blogs<br>Partners<br>FAQ<br>Contact</div>
  <div class="abs col" style="left:871px"><h4>QUESTIONS</h4></div>
  <svg class="abs" style="left:874px;top:106px" width="22" height="22" viewBox="0 0 24 24" fill="none" stroke="#ddd" stroke-width="1.6"><path d="M5 2h4l2 5-3 2a12 12 0 0 0 7 7l2-3 5 2v4a2 2 0 0 1-2 2A18 18 0 0 1 3 4a2 2 0 0 1 2-2z"/></svg>
  <div class="abs col" style="left:910px;top:102px;line-height:20px">Call Us Now<br><span style="font-size:17px;color:#fff">(600) 555 0142</span></div>
  <svg class="abs" style="left:874px;top:176px" width="24" height="18" viewBox="0 0 24 18" fill="none" stroke="#ddd" stroke-width="1.6"><rect x="1" y="1" width="22" height="16"/><path d="M1 1l11 9 11-9"/></svg>
  <div class="abs col" style="left:910px;top:170px;line-height:22px">Email Us<br><span style="font-size:15px;color:#fff">hello@zarvio.tv</span></div>
</footer>

<div class="abs copyright" style="left:0;width:1200px">Copyright © 2020 All right reserved</div>

</body>
</html>
```